Bref créative
Velvet Rooms
Home Interiors
Modern
Linnea Parcot Weller
Design Consultant
412 Quillon Lane
Palm beach Gardens, Fl 33587
LinneaParcot@velmorra.example
VelvetRooms.example
My logo is the Velvet Rooms. Would like to incorporate a flur de lis.

```html
<!DOCTYPE html>
<html lang="en">
<head>
<meta charset="UTF-8">
<title>Velvet Rooms — Business Card</title>
<link rel="stylesheet" href="https://fonts.googleapis.com/css2?family=PT+Serif:wght@400;700&display=swap">
<style>
  :root {
    --page-bg: #ece8e3;
    --card-white: #ffffff;
    --brand-red: #c3161c;
    --brand-red-dark: #8e0d12;
    --swoosh-black: #111111;
    --logo-grey: #3a3a3a;
    --text-muted: #444444;
    --text-light: #ffffff;
  }
  * { margin: 0; padding: 0; box-sizing: border-box; }
  html, body {
    width: 1200px; height: 780px; overflow: hidden;
    background: var(--page-bg);
    font-family: "PT Serif", Georgia, serif;
  }
  .card {
    position: absolute; left: 100px; top: 100px;
    width: 1000px; height: 580px;
    background: var(--card-white);
    border-radius: 26px; overflow: hidden;
    box-shadow: 0 10px 30px rgba(0,0,0,0.18);
  }
  .card-bands { position: absolute; inset: 0; }
  .holder { position: absolute; right: 56px; top: 40px; text-align: right; }
  .holder-name { color: var(--brand-red); font-weight: 700; font-size: 40px; line-height: 1.1; }
  .holder-role { color: var(--text-muted); font-size: 24px; margin-top: 6px; }
  .brand { position: absolute; left: 44px; top: 130px; display: flex; align-items: center; gap: 18px; }
  .brand-emblem {
    width: 120px; height: 260px;
    background: linear-gradient(180deg, #d9262b 0%, #e9e9e9 30%, #c8c8c8 100%);
    border-radius: 8px;
  }
  .brand-name {
    color: var(--logo-grey); font-weight: 400; font-size: 46px; line-height: 1.05;
    font-variant: small-caps; letter-spacing: 1px; margin-bottom: 40px;
  }
  .brand-line { display: block; }
  .contact {
    position: absolute; right: 56px; top: 330px;
    color: var(--text-light); text-align: right; font-size: 23px; line-height: 1.5;
  }
  .contact-row { display: flex; justify-content: flex-end; align-items: center; gap: 22px; }
  .contact-item { display: inline-flex; align-items: center; gap: 8px; }
  .contact-address { margin-bottom: 12px; }
  .contact-phones { margin-bottom: 14px; font-size: 25px; }
  .icon { width: 22px; height: 22px; fill: var(--text-light); }
</style>
</head>
<body>
  <div class="card">
    <svg class="card-bands" viewBox="0 0 1000 580" preserveAspectRatio="none" aria-hidden="true">
      <defs>
        <linearGradient id="band-red" x1="0" y1="1" x2="1" y2="0">
          <stop offset="0" stop-color="var(--brand-red-dark)"/>
          <stop offset="0.6" stop-color="var(--brand-red)"/>
          <stop offset="1" stop-color="var(--brand-red-dark)"/>
        </linearGradient>
      </defs>
      <path d="M0,445 C300,565 700,305 1000,175 L1000,580 L0,580 Z" fill="url(#band-red)"/>
      <path d="M0,425 C300,548 700,288 1000,150 L1000,175 C700,305 300,565 0,445 Z" fill="var(--swoosh-black)"/>
    </svg>

    <div class="holder">
      <div class="holder-name">Linnea Parcot Weller</div>
      <div class="holder-role">Design Consultant</div>
    </div>

    <div class="brand">
      <div class="brand-emblem" role="img" aria-label="Brand illustration: vase with red flowers"></div>
      <div class="brand-name">
        <span class="brand-line">Velvet</span>
        <span class="brand-line">Rooms, LLC</span>
      </div>
    </div>

    <div class="contact">
      <div class="contact-address">412 Quillon Lane<br>Palm beach Gardens, Fl 33587</div>
      <div class="contact-row contact-phones">
        <span class="contact-item">
          <svg class="icon" viewBox="0 0 24 24"><rect x="6" y="2" width="12" height="20" rx="2"/><rect x="8" y="4" width="8" height="11" fill="var(--brand-red)"/></svg>
          561.555.0142
        </span>
        <span class="contact-item">
          <svg class="icon" viewBox="0 0 24 24"><path d="M3 9c0-3 4-5 9-5s9 2 9 5v2h-5V9H8v2H3z"/><rect x="5" y="12" width="14" height="9" rx="2"/></svg>
          561.555.0187
        </span>
      </div>
      <div class="contact-row">
        <span class="contact-item">
          <svg class="icon" viewBox="0 0 24 24"><circle cx="12" cy="12" r="10"/><circle cx="12" cy="12" r="4" fill="var(--brand-red)"/></svg>
          LinneaParcot@velmorra.example
        </span>
        <span class="contact-item">
          <svg class="icon" viewBox="0 0 24 24"><circle cx="12" cy="12" r="10"/><path d="M2 12h20M12 2v20" stroke="var(--brand-red)" stroke-width="1.8"/></svg>
          VelvetRooms.example
        </span>
      </div>
    </div>
  </div>
</body>
</html>
```